Business Card design for new private practice opening

I need a business card design for my new private practice with my new logo uploaded as a file
On the front the logo
On the back: maybe a small logo somewhere?
Priv. Doz. DDr. Corinna Vestaluk
Fachärztin für Allgemein- & Viszeralchirurgie
Address: xxx
Tel: xxx
Mobil:xxx
Webseite:xxx
Email:xxx

Contact Information for Business Card

See project description above for details

Requirements
Nice to have
• I would like the colors of the logo incorporated into the business card

```html
<!DOCTYPE html>
<html lang="de">
<head>
<meta charset="utf-8">
<title>Vestaluk Chirurgie – Visitenkarte</title>
<link rel="stylesheet" href="https://fonts.googleapis.com/css2?family=Poppins:wght@400;500;600;700&display=swap">
<style>
  :root {
    --teal: #48b8b6;
    --grey: #8a8a8a;
    --ink: #1e1e1e;
    --paper: #ffffff;
    --backdrop: #ece9e4;
  }
  html, body {
    margin: 0;
    width: 1200px;
    height: 900px;
    overflow: hidden;
    background: var(--backdrop);
    font-family: "Poppins", sans-serif;
  }
  .canvas {
    position: relative;
    width: 1200px;
    height: 900px;
  }
  .card {
    position: absolute;
    width: 600px;
    height: 350px;
    box-shadow: 0 6px 18px rgba(0,0,0,.18);
    overflow: hidden;
  }
  .card-front {
    left: 300px;
    top: 65px;
    background: var(--teal);
    display: flex;
    align-items: center;
    justify-content: center;
    gap: 30px;
  }
  .brand-disc {
    width: 118px;
    height: 118px;
    border: 5px solid var(--paper);
    border-radius: 50%;
    box-sizing: border-box;
  }
  .brand-name {
    color: var(--paper);
    font-weight: 600;
    font-size: 44px;
    line-height: 1.05;
    letter-spacing: 1px;
    margin: 0;
  }
  .card-back {
    left: 300px;
    top: 480px;
    background: var(--paper);
  }
  .back-swoosh {
    position: absolute;
    inset: 0;
  }
  .back-disc {
    position: absolute;
    right: 40px;
    top: 30px;
    width: 140px;
    height: 140px;
    border: 5px solid var(--grey);
    border-radius: 50%;
    box-sizing: border-box;
  }
  .contact-block {
    position: absolute;
    left: 40px;
    top: 46px;
    color: var(--ink);
  }
  .doctor-name {
    margin: 0;
    color: var(--teal);
    font-weight: 600;
    font-size: 17px;
  }
  .doctor-title {
    margin: 2px 0 0;
    font-size: 14px;
    line-height: 1.3;
  }
  .contact-list {
    list-style: none;
    margin: 22px 0 0;
    padding: 0;
    font-size: 15px;
    line-height: 1.45;
  }
  .contact-list li {
    display: flex;
    align-items: center;
    gap: 8px;
  }
  .contact-icon {
    width: 18px;
    height: 18px;
    flex: none;
  }
  .address {
    margin: 12px 0 0 26px;
    font-size: 15px;
    line-height: 1.3;
  }
  .website {
    position: absolute;
    right: 36px;
    bottom: 40px;
    color: var(--paper);
    font-size: 14px;
    margin: 0;
  }
</style>
</head>
<body>
<main class="canvas">

  <section class="card card-front" aria-label="Vorderseite">
    <div class="brand-disc"></div>
    <h1 class="brand-name">VESTALUK<br>CHIRURGIE</h1>
  </section>

  <section class="card card-back" aria-label="Rückseite">
    <svg class="back-swoosh" viewBox="0 0 600 350" preserveAspectRatio="none" aria-hidden="true">
      <path d="M0 300 C 180 300 300 270 420 200 C 480 165 540 140 600 130 L600 350 L0 350 Z" fill="var(--teal)"/>
      <path d="M0 280 C 170 280 300 255 450 175 C 330 250 200 292 0 300 Z" fill="var(--grey)"/>
    </svg>

    <div class="back-disc"></div>

    <div class="contact-block">
      <h2 class="doctor-name">Priv. Doz. DDr. Corinna Vestaluk</h2>
      <p class="doctor-title">Fachärztin für Allgemein- &amp;<br>Viszeralchirurgie</p>
      <ul class="contact-list">
        <li>
          <svg class="contact-icon" viewBox="0 0 20 20" aria-label="Telefon"><circle cx="10" cy="10" r="9" fill="none" stroke="var(--teal)" stroke-width="1.5"/><path d="M6.5 6c0 4 3.5 7.5 7.5 7.5l.8-1.8-2-1-1 1c-1.5-.6-2.5-1.6-3-3l1-1-1-2z" fill="var(--teal)"/></svg>
          <span>044-987 654 321</span>
        </li>
        <li>
          <svg class="contact-icon" viewBox="0 0 20 20" aria-label="Mobil"><circle cx="10" cy="10" r="9" fill="none" stroke="var(--teal)" stroke-width="1.5"/><rect x="7" y="5" width="6" height="10" rx="1" fill="none" stroke="var(--teal)" stroke-width="1.4"/></svg>
          <span>044-987 654 322</span>
        </li>
        <li>
          <svg class="contact-icon" viewBox="0 0 20 20" aria-label="E-Mail"><circle cx="10" cy="10" r="9" fill="none" stroke="var(--teal)" stroke-width="1.5"/><rect x="5.5" y="7" width="9" height="6.5" fill="none" stroke="var(--teal)" stroke-width="1.3"/><path d="M5.5 7l4.5 3.5L14.5 7" fill="none" stroke="var(--teal)" stroke-width="1.3"/></svg>
          <span>info@vestaluk-praxis.com</span>
        </li>
      </ul>
      <p class="address">421, Address line goes here<br>45452, Country Name</p>
    </div>

    <p class="website">www.vestaluk-chirurgie.com</p>
  </section>

</main>
</body>
</html>
```